Introduction:
We are an Australia-based Cyber Security Penetration testing company seeking a website redesign to showcase our services, expertise, and experience. Our target audience includes businesses and organizations of all sizes who are seeking to secure their IT infrastructure against cyber threats. The purpose of the website redesign is to increase our online presence, generate leads, and establish our company as a trusted authority in the industry.
Objectives:
Create a professional and modern website that is easy to navigate and user-friendly.
Provide information about our company, services, and expertise.
Clearly display table of our 3 services: Bug Bounty as a Service, Penetration Testing and Code Review.
Generate leads through online contact forms and calls-to-action.
Optimize the website for search engines to increase visibility and traffic.
Website similar to: https://www.velmoro.com.au/.
Target Audience:
Our target audience includes businesses and organizations of all sizes that require cybersecurity penetration testing services. These include:
Small and medium-sized enterprises (SMEs)
Australian Government agencies
Design Requirements:
Clean, modern, and professional design.
Use of colors that convey trust, reliability, and expertise (such as orange and grey).
Calls-to-action that encourage visitors to contact us or request a quote.
Integration with social media channels to increase engagement and brand awareness.
A blog section to showcase our thought leadership and expertise.
A news section to share updates about our company and the industry.
Content Requirements:
Home page that introduces our company and services and highlights our expertise.
About Us page that provides information about our company, team, and values.
Services page that lists our services and explains the benefits of each.
Case Studies page that showcases our previous work and success stories.
Contact Us page that includes a contact form, phone number, and email address.
Blog section with articles related to the cybersecurity industry and our services.
News section with updates about our company and the industry.
Look and feel
Each slider illustrates characteristics of the customer's brand and the style your logo design should communicate.

```html
<!DOCTYPE html>
<html lang="en">
<head>
<meta charset="utf-8">
<title>Cindercloud — Cyber Security</title>
<link href="https://fonts.googleapis.com/css2?family=Poppins:wght@300;400;500;600;700;800&display=swap" rel="stylesheet">
<style>
:root{
  --orange:#f26a22;
  --orange-dark:#d9561a;
  --ink:#2b2b2b;
  --text:#555;
  --muted:#888;
  --grey-bg:#f3f3f3;
  --cloud:#f1f1f1;
  --dark:#262626;
  --white:#fff;
}
*{box-sizing:border-box;margin:0;padding:0}
html,body{width:1200px;height:4236px;overflow:hidden}
body{font-family:"Poppins",sans-serif;color:var(--ink);background:var(--white);position:relative}
a{color:inherit;text-decoration:none}

/* header */
.site-header{position:absolute;left:0;top:0;width:1200px;height:115px;background:var(--white)}
.brand{position:absolute;left:110px;top:28px;display:flex;align-items:center;gap:12px;font-weight:600;font-size:32px;color:var(--orange)}
.brand-dot{width:22px;height:22px;border-radius:50%;background:var(--orange)}
.header-call{position:absolute;right:112px;top:20px;font-size:16px;font-weight:500;display:flex;align-items:center;gap:6px}
.main-nav{position:absolute;right:112px;top:70px;display:flex;gap:23px;font-size:17px;font-weight:500}
.main-nav .active{color:var(--orange)}

/* hero */
.hero{position:absolute;left:0;top:115px;width:1200px;height:617px;
  background:linear-gradient(100deg,#1a1c22 0%,#3a2a20 35%,#8a4a22 52%,#2b3a4a 75%,#1b2430 100%)}
.hero-kicker{position:absolute;left:110px;top:145px;color:var(--white);font-size:30px;font-weight:500}
.hero-title{position:absolute;left:110px;top:205px;color:var(--white);font-size:58px;font-weight:800;line-height:68px}
.btn{display:inline-flex;align-items:center;justify-content:center;background:var(--orange);color:var(--white);font-weight:600;border-radius:40px;text-transform:uppercase}
.hero .btn{position:absolute;left:110px;top:370px;width:237px;height:63px;font-size:18px}

/* welcome */
.welcome{position:absolute;left:0;top:732px;width:1200px;height:460px}
.welcome-cloud{position:absolute;left:0;top:24px}
.welcome-title{position:absolute;left:110px;top:160px;font-size:38px;font-weight:600;line-height:56px}
.welcome-title span{color:var(--orange)}
.watch{position:absolute;left:110px;top:298px;display:flex;align-items:center;gap:12px;font-size:15px;font-weight:600}
.watch-icon{width:52px;height:52px;border-radius:50%;border:2px solid #bbb;display:flex;align-items:center;justify-content:center}
.welcome-copy{position:absolute;left:562px;top:68px;width:530px;font-size:15px;line-height:27px;color:var(--text)}
.welcome-copy p+p{margin-top:26px}
.welcome .btn{position:absolute;left:562px;top:317px;width:150px;height:56px;font-size:17px}

/* services */
.services{position:absolute;left:0;top:1192px;width:1200px;height:750px}
.services-band{position:absolute;left:0;top:0;width:1200px;height:403px;background:linear-gradient(120deg,var(--orange) 0%,#f07a2c 50%,var(--orange-dark) 100%)}
.section-title{font-size:40px;font-weight:600;text-transform:uppercase}
.section-title span{color:var(--orange)}
.services .section-title{position:absolute;left:0;width:1200px;top:76px;text-align:center;color:var(--white)}
.service-card{position:absolute;top:171px;width:306px;text-align:center}
.service-photo{width:306px;height:232px}
.service-body{position:relative;margin:-42px 18px 0;background:var(--white);padding:22px 4px 0}
.service-icon{display:block;margin:0 auto}
.service-name{font-size:22px;font-weight:500;line-height:30px;margin-top:22px}
.service-desc{font-size:15px;line-height:27px;color:var(--text);margin-top:12px}
.read-more{display:block;margin-top:20px;color:var(--orange);font-weight:600;font-size:16px}

/* expertise */
.expertise{position:absolute;left:0;top:1943px;width:1200px;height:608px;background:var(--grey-bg)}
.expertise-photo{position:absolute;left:0;top:0;width:503px;height:608px;background:radial-gradient(circle at 50% 50%,#c96a3a 0%,#4a3a4a 45%,#1e2636 100%)}
.expertise .section-title{position:absolute;left:564px;top:64px;font-size:40px}
.expertise-intro{position:absolute;left:564px;top:135px;width:440px;font-size:15px;line-height:27px;color:var(--text)}
.skill{position:absolute;display:flex;align-items:center;gap:16px;font-size:19px;font-weight:500;line-height:25px}
.skill-badge{width:98px;height:98px;border-radius:50%;background:var(--white);box-shadow:0 2px 10px rgba(0,0,0,.08);display:flex;align-items:center;justify-content:center;flex:none}
.col-a{left:564px}
.col-b{left:816px}
.row-1{top:219px}
.row-2{top:338px}
.row-3{top:456px}

/* blog */
.blog{position:absolute;left:0;top:2551px;width:1200px;height:688px;overflow:hidden}
.blog .section-title{position:absolute;left:0;width:1200px;top:88px;text-align:center}
.post{position:absolute;top:191px;width:313px}
.post-photo{width:313px;height:232px}
.post-title{font-size:21px;font-weight:600;margin-top:26px;white-space:nowrap}
.post-meta{font-size:15px;color:var(--text);margin-top:8px;display:flex;align-items:center;gap:6px;white-space:nowrap}
.post-meta svg{flex:none}
.post-text{font-size:15px;line-height:27px;color:var(--text);margin-top:12px;padding-left:2px}
.post.faded{opacity:.35}
.slider-arrow{position:absolute;top:278px;width:56px;height:56px;border-radius:50%;background:var(--white);box-shadow:0 2px 8px rgba(0,0,0,.2);display:flex;align-items:center;justify-content:center}

/* cta */
.cta{position:absolute;left:0;top:3239px;width:1200px;height:588px;background:linear-gradient(180deg,#1f1f1f 0%,#2a2a2a 55%,#4a4a4a 100%)}
.cta-title{position:absolute;left:110px;top:140px;color:var(--white);font-size:38px;font-weight:600;line-height:56px;text-transform:uppercase}
.cta-title span{color:var(--orange)}
.cta-sub{position:absolute;left:110px;top:325px;color:var(--white);font-size:24px}
.contact-form{position:absolute;left:602px;top:61px;width:486px}
.field{display:block;width:486px;height:50px;background:var(--white);border-radius:3px;margin-bottom:14px;padding:13px 15px;font-size:15px;color:#777}
.field.area{height:117px}
.cta .btn{margin-top:19px;margin-left:3px;width:120px;height:51px;font-size:17px}

/* footer */
.site-footer{position:absolute;left:0;top:3827px;width:1200px;height:409px}
.footer-brand{position:absolute;left:110px;top:140px;display:flex;align-items:center;gap:16px;font-size:58px;font-weight:600;color:var(--orange)}
.footer-brand .brand-dot{width:40px;height:40px}
.footer-col{position:absolute;top:54px}
.footer-col h4{font-size:18px;font-weight:600;margin-bottom:14px}
.footer-col li{list-style:none;font-size:15px;line-height:26.6px;color:var(--text)}
.contact-line{display:flex;gap:8px;font-size:15px;color:var(--text);line-height:26px;margin-bottom:26px}
.footer-rule{position:absolute;left:110px;top:299px;width:978px;height:1px;background:#ccc}
.copyright{position:absolute;left:110px;top:338px;font-size:15px;color:var(--text)}
.social{position:absolute;top:328px;width:44px;height:44px;border-radius:50%;border:2px solid var(--orange)}
</style>
</head>
<body>

<header class="site-header">
  <div class="brand"><span class="brand-dot"></span>Cindercloud</div>
  <div class="header-call">
    <svg width="14" height="14" viewBox="0 0 24 24"><path fill="#f26a22" d="M6.6 10.8a15 15 0 0 0 6.6 6.6l2.2-2.2c.3-.3.7-.4 1-.2 1.1.4 2.3.6 3.6.6.6 0 1 .4 1 1V20c0 .6-.4 1-1 1A17 17 0 0 1 3 4c0-.6.4-1 1-1h3.5c.6 0 1 .4 1 1 0 1.3.2 2.5.6 3.6.1.3 0 .7-.2 1z"/></svg>
    Call: 1 800 555 0142
  </div>
  <nav class="main-nav">
    <a class="active">Home</a><a>About Us</a><a>Services</a><a>Case Studies</a><a>Blog</a><a>News</a><a>Contact Us</a>
  </nav>
</header>

<section class="hero" role="img" aria-label="Photo of a cyber security team reviewing data on a tablet in a dark office with glowing screens">
  <div class="hero-kicker">Cyber Security</div>
  <h1 class="hero-title">PENETRATION<br>TESTING</h1>
  <a class="btn">Request a Quote</a>
</section>

<section class="welcome">
  <svg class="welcome-cloud" width="500" height="400" viewBox="0 0 500 400" aria-hidden="true">
    <path fill="#f1f1f1" d="M0 200 C40 160 70 130 80 95 C110 20 200 -10 280 20 C340 40 370 90 380 130 C450 140 490 180 490 250 C490 330 440 375 360 375 L60 375 C30 375 0 365 0 340 Z"/>
  </svg>
  <h2 class="welcome-title">WELCOME TO<br><span>CINDERCLOUD</span></h2>
  <div class="watch">
    <span class="watch-icon"><svg width="22" height="24" viewBox="0 0 22 24"><path fill="#f26a22" d="M2 1l19 11L2 23z"/></svg></span>
    WATCH OUR VIDEO
  </div>
  <div class="welcome-copy">
    <p>Lorem ipsum dolor sit amet, consectetur adipiscing elit, sed seido eiusmod tempor incididunt ut lab.</p>
    <p>Sore et dolore magna aliqua. Quis ipsum suspendisse ultrices gra vida. Risus commodo viverra maecenas accumsan lacusgtil vel facilisis vel eum iure reprehenderit qui in ea voluptate velit egsse quam nihil molestiae consequatur, vel illum qui dolorem eujiluim fugiat quo voluptas nulla pas.</p>
  </div>
  <a class="btn">Read More</a>
</section>

<section class="services">
  <div class="services-band"></div>
  <h2 class="section-title">Services We Provide</h2>

  <article class="service-card" style="left:112px">
    <div class="service-photo" role="img" aria-label="Photo of a glowing digital padlock on a circuit background" style="background:radial-gradient(circle,#e0582a 0%,#0f3a4a 45%,#0a1c26 100%)"></div>
    <div class="service-body">
      <svg class="service-icon" width="90" height="90" viewBox="0 0 90 90" fill="none" stroke="#444" stroke-width="2.5">
        <rect x="6" y="6" width="70" height="58" rx="3"/><line x1="6" y1="16" x2="76" y2="16"/>
        <circle cx="55" cy="52" r="24" fill="#fff"/><circle cx="55" cy="52" r="12" stroke="#f26a22"/><path d="M55 40v24M43 52h24" stroke="#f26a22"/>
        <line x1="14" y1="28" x2="30" y2="28"/><line x1="14" y1="38" x2="26" y2="38"/>
      </svg>
      <h3 class="service-name">Bug Bounty as<br>a Service</h3>
      <p class="service-desc">Nam libero tempore, cum soluta nobis est eligendi optio cumque nihil imedit quo</p>
      <a class="read-more">READ MORE</a>
    </div>
  </article>

  <article class="service-card" style="left:447px">
    <div class="service-photo" role="img" aria-label="Photo of two engineers looking at a tablet in front of data screens" style="background:linear-gradient(120deg,#1c2c3a 0%,#4c6a7c 50%,#22303c 100%)"></div>
    <div class="service-body">
      <svg class="service-icon" width="90" height="90" viewBox="0 0 90 90" fill="none" stroke="#444" stroke-width="2.5">
        <rect x="6" y="40" width="34" height="44" rx="2"/><line x1="13" y1="52" x2="33" y2="52"/><line x1="13" y1="62" x2="33" y2="62"/><line x1="13" y1="72" x2="33" y2="72"/>
        <rect x="46" y="32" width="34" height="30" rx="3"/><path d="M53 32v-10a10 10 0 0 1 20 0v10"/><circle cx="63" cy="46" r="4" stroke="#f26a22"/>
      </svg>
      <h3 class="service-name">Penetration<br>Testing</h3>
      <p class="service-desc">Nam libero tempore, cum soluta nobis est eligendi optio cumque nihil imedit quo</p>
      <a class="read-more">READ MORE</a>
    </div>
  </article>

  <article class="service-card" style="left:783px">
    <div class="service-photo" role="img" aria-label="Photo of a glowing fingerprint scan under streams of code" style="background:linear-gradient(180deg,#0b1418 0%,#10343a 60%,#1bb4a8 100%)"></div>
    <div class="service-body">
      <svg class="service-icon" width="110" height="90" viewBox="0 0 110 90" fill="none" stroke="#444" stroke-width="2.5">
        <rect x="8" y="10" width="94" height="68" rx="3"/><line x1="8" y1="22" x2="102" y2="22"/>
        <circle cx="28" cy="50" r="14" stroke="#f26a22"/><path d="M21 50l5 5 9-10" stroke="#f26a22"/>
        <path d="M56 40l-8 10 8 10M86 40l8 10-8 10M76 36l-10 28"/>
      </svg>
      <h3 class="service-name">Code<br>Review</h3>
      <p class="service-desc">Nam libero tempore, cum soluta nobis est eligendi optio cumque nihil imedit quo</p>
      <a class="read-more">READ MORE</a>
    </div>
  </article>
</section>

<section class="expertise">
  <div class="expertise-photo" role="img" aria-label="Photo of hands on a laptop with a glowing security padlock and network icons"></div>
  <h2 class="section-title">Our <span>Expertise</span></h2>
  <p class="expertise-intro">Lorem ipsum dolor sit amet, consectetur adipi dertsc deing elit, sed seido eiusmod tem.</p>

  <div class="skill col-a row-1">
    <span class="skill-badge"><svg width="50" height="50" viewBox="0 0 50 50" fill="none" stroke="#f26a22" stroke-width="2"><circle cx="25" cy="18" r="10"/><circle cx="25" cy="18" r="4"/><path d="M6 32l19 10 19-10M6 38l19 10 19-10"/></svg></span>
    Transparent<br>Processes
  </div>
  <div class="skill col-b row-1">
    <span class="skill-badge"><svg width="50" height="50" viewBox="0 0 50 50" fill="none" stroke="#f26a22" stroke-width="2"><circle cx="25" cy="16" r="8"/><path d="M25 2v4M12 8l3 3M38 8l-3 3M14 44V30l11 6 11-6v14z"/></svg></span>
    Real World<br>Testing
  </div>
  <div class="skill col-a row-2">
    <span class="skill-badge"><svg width="50" height="50" viewBox="0 0 50 50" fill="none" stroke="#f26a22" stroke-width="2"><circle cx="25" cy="18" r="7"/><path d="M12 44c0-9 6-14 13-14s13 5 13 14M8 8l2 4 4 1-3 3 1 4-4-2-4 2 1-4-3-3 4-1zM40 8l2 4 4 1-3 3 1 4-4-2-4 2 1-4-3-3 4-1z"/></svg></span>
    Expert<br>Skillsets
  </div>
  <div class="skill col-b row-2">
    <span class="skill-badge"><svg width="50" height="50" viewBox="0 0 50 50" fill="none" stroke="#f26a22" stroke-width="2"><rect x="8" y="8" width="34" height="26" rx="2"/><rect x="18" y="16" width="14" height="12" rx="2"/><path d="M4 40h42M20 16v-3a5 5 0 0 1 10 0v3"/></svg></span>
    Pre-assessment
  </div>
  <div class="skill col-a row-3">
    <span class="skill-badge"><svg width="50" height="50" viewBox="0 0 50 50" fill="none" stroke="#f26a22" stroke-width="2"><rect x="10" y="4" width="30" height="42" rx="2"/><path d="M16 14h18M16 22h18M16 30h18M16 38h10"/></svg></span>
    Report
  </div>
  <div class="skill col-b row-3">
    <span class="skill-badge"><svg width="50" height="50" viewBox="0 0 50 50" fill="none" stroke="#f26a22" stroke-width="2"><rect x="6" y="6" width="28" height="36" rx="2"/><path d="M12 14h16M12 22h8"/><circle cx="32" cy="32" r="9"/><path d="M38 38l8 8"/></svg></span>
    Reconnaissance
  </div>
</section>

<section class="blog">
  <h2 class="section-title">Our <span>Blog</span></h2>

  <article class="post" style="left:110px">
    <div class="post-photo" role="img" aria-label="Photo of colleagues reviewing a monitor in a dim office" style="background:linear-gradient(120deg,#2a3440 0%,#6a7c8c 50%,#c9c2b8 100%)"></div>
    <h3 class="post-title">Finibus Bonoruet Malorum</h3>
    <div class="post-meta"><svg width="14" height="14" viewBox="0 0 14 14"><rect x="1" y="2" width="12" height="11" rx="1" fill="#f26a22"/></svg>Sep 19, 2022 &nbsp;| <svg width="12" height="14" viewBox="0 0 12 14"><circle cx="6" cy="4" r="3.5" fill="#f26a22"/><path d="M0 14c0-4 3-6 6-6s6 2 6 6z" fill="#f26a22"/></svg>Admin</div>
    <p class="post-text">Nam libero tempore, cum soluta nob is est eligendi optio cumque nihil imp edit quo minus id quo.</p>
  </article>
  <article class="post" style="left:444px">
    <div class="post-photo" role="img" aria-label="Photo of source code on a screen seen through a lens" style="background:linear-gradient(135deg,#14181e 0%,#3a4250 50%,#1a1e24 100%)"></div>
    <h3 class="post-title">Finibus Bonoruet Malorum</h3>
    <div class="post-meta"><svg width="14" height="14" viewBox="0 0 14 14"><rect x="1" y="2" width="12" height="11" rx="1" fill="#f26a22"/></svg>Sep 19, 2022 &nbsp;| <svg width="12" height="14" viewBox="0 0 12 14"><circle cx="6" cy="4" r="3.5" fill="#f26a22"/><path d="M0 14c0-4 3-6 6-6s6 2 6 6z" fill="#f26a22"/></svg>Admin</div>
    <p class="post-text">Nam libero tempore, cum soluta nob is est eligendi optio cumque nihil imp edit quo minus id quo.</p>
  </article>
  <article class="post" style="left:776px">
    <div class="post-photo" role="img" aria-label="Photo of a laptop with glowing blue security icons" style="background:linear-gradient(135deg,#0c2236 0%,#1e5a8a 50%,#0e2030 100%)"></div>
    <h3 class="post-title">Finibus Bonoruet Malorum</h3>
    <div class="post-meta"><svg width="14" height="14" viewBox="0 0 14 14"><rect x="1" y="2" width="12" height="11" rx="1" fill="#f26a22"/></svg>Sep 19, 2022 &nbsp;| <svg width="12" height="14" viewBox="0 0 12 14"><circle cx="6" cy="4" r="3.5" fill="#f26a22"/><path d="M0 14c0-4 3-6 6-6s6 2 6 6z" fill="#f26a22"/></svg>Admin</div>
    <p class="post-text">Nam libero tempore, cum soluta nob is est eligendi optio cumque nihil imp edit quo minus id quo.</p>
  </article>
  <article class="post faded" style="left:1110px">
    <div class="post-photo" role="img" aria-label="Photo of a workspace with devices" style="background:linear-gradient(135deg,#8a8f96 0%,#c6c9cc 100%)"></div>
    <h3 class="post-title">Finibus Bonoruet Malorum</h3>
    <div class="post-meta">Sep 19, 2022 | Admin</div>
    <p class="post-text">Nam libero tempore, cum soluta nob is est eligendi optio cumque nihil imp edit quo minus id quo.</p>
  </article>

  <span class="slider-arrow" style="left:84px"><svg width="14" height="20" viewBox="0 0 14 20"><path d="M11 2L3 10l8 8" fill="none" stroke="#444" stroke-width="2.5"/></svg></span>
  <span class="slider-arrow" style="left:1049px"><svg width="14" height="20" viewBox="0 0 14 20"><path d="M3 2l8 8-8 8" fill="none" stroke="#444" stroke-width="2.5"/></svg></span>
</section>

<section class="cta">
  <h2 class="cta-title">Defend your business<br>against the latest<br><span>Cyber-threats</span></h2>
  <p class="cta-sub">Get in touch with us today!</p>
  <form class="contact-form">
    <span class="field">Name</span>
    <span class="field">Email</span>
    <span class="field">Phone</span>
    <span class="field">Company</span>
    <span class="field area">How can we help?</span>
    <span class="btn">Submit</span>
  </form>
</section>

<footer class="site-footer">
  <div class="footer-brand"><span class="brand-dot"></span>Cindercloud</div>
  <div class="footer-col" style="left:557px">
    <h4>Quick Links</h4>
    <ul><li>Home</li><li>About Us</li><li>Services</li><li>Case Studies</li><li>Blog</li><li>News</li><li>Contact Us</li></ul>
  </div>
  <div class="footer-col" style="left:773px">
    <h4>Contact Information</h4>
    <div class="contact-line"><svg width="12" height="16" viewBox="0 0 12 16" style="margin-top:5px;flex:none"><path fill="#f26a22" d="M6 0a6 6 0 0 0-6 6c0 4.5 6 10 6 10s6-5.5 6-10a6 6 0 0 0-6-6zm0 8.5A2.5 2.5 0 1 1 6 3.5a2.5 2.5 0 0 1 0 5z"/></svg><span>Suite 9, 212 Harbour Lane,<br>&nbsp;&nbsp;&nbsp;Ashford Park, VIC 3999</span></div>
    <div class="contact-line"><svg width="14" height="14" viewBox="0 0 24 24" style="margin-top:6px;flex:none"><path fill="#f26a22" d="M6.6 10.8a15 15 0 0 0 6.6 6.6l2.2-2.2c.3-.3.7-.4 1-.2 1.1.4 2.3.6 3.6.6.6 0 1 .4 1 1V20c0 .6-.4 1-1 1A17 17 0 0 1 3 4c0-.6.4-1 1-1h3.5c.6 0 1 .4 1 1 0 1.3.2 2.5.6 3.6.1.3 0 .7-.2 1z"/></svg>1 800 555 0142</div>
    <div class="contact-line"><svg width="16" height="12" viewBox="0 0 16 12" style="margin-top:7px;flex:none"><rect width="16" height="12" rx="1" fill="#f26a22"/><path d="M1 1l7 6 7-6" fill="none" stroke="#fff" stroke-width="1.5"/></svg>info@cindercloud.example</div>
  </div>
  <div class="footer-rule"></div>
  <p class="copyright">Copyright © - 2023, Cindercloud, All Rights Reserved</p>
  <span class="social" style="left:992px" aria-label="Social profile"></span>
  <span class="social" style="left:1044px" aria-label="Social profile"></span>
</footer>

</body>
</html>
```